Art Deco Wedding Invitation

We need a wedding invitation designed for a 1920's Art Deco theme.
The wedding will take place in Berlin, which had a glamorous, modern and wild culture in the 1920's. This may offer some design inspiration.
The couple's names are Rowan and Liesel and the wedding will take place on May 8, 2015.

Industry/Entity Type

Wedding

```html
<!DOCTYPE html>
<html lang="en">
<head>
<meta charset="utf-8">
<title>Rowan &amp; Liesel – Art Deco Wedding Invitation</title>
<link rel="stylesheet" href="https://fonts.googleapis.com/css2?family=Limelight&family=Poiret+One&display=swap">
<style>
  :root {
    --gold: #8f7a45;
    --gold-light: #b0a274;
    --gold-pale: #cfc3a0;
    --ink: #111111;
    --paper: #ffffff;
    --backdrop: #e9e6df;
  }
  * { box-sizing: border-box; margin: 0; padding: 0; }
  html, body { width: 1200px; height: 1155px; overflow: hidden; }
  body {
    background: var(--backdrop);
    position: relative;
    font-family: "Poiret One", sans-serif;
    color: var(--ink);
  }
  .card {
    position: absolute;
    background: var(--paper);
    overflow: hidden;
  }

  /* Cover card */
  .cover { left: 25px; top: 25px; width: 416px; height: 540px; }
  .cover-circles {
    position: absolute; right: 0; top: 0; width: 175px; height: 185px;
    background: radial-gradient(circle at 60% 45%, var(--gold) 0%, var(--gold-light) 70%, var(--paper) 100%);
    border-bottom-left-radius: 90px;
  }
  .cover-names {
    position: absolute; left: 0; right: 0; top: 242px;
    text-align: center;
    font-family: "Limelight", serif;
    font-size: 34px; letter-spacing: 3px;
    color: var(--gold);
    text-transform: uppercase;
  }

  /* Pattern card */
  .pattern-card { left: 25px; top: 590px; width: 416px; height: 540px; }
  .pattern-fill {
    position: absolute; inset: 0;
    background: radial-gradient(circle at 50% 50%, var(--gold-light) 0%, var(--gold-pale) 100%);
  }

  /* Invitation card */
  .invitation { left: 475px; top: 123px; width: 700px; height: 909px; }
  .invite-circles {
    position: absolute; left: 0; right: 0; top: 0; height: 291px;
    background: linear-gradient(to bottom, var(--gold) 0%, var(--gold-light) 80%, var(--gold-pale) 100%);
    border-bottom-left-radius: 60px 40px;
    border-bottom-right-radius: 60px 40px;
  }
  .invite-names {
    position: absolute; left: 0; right: 0; top: 335px;
    text-align: center;
    font-family: "Limelight", serif;
    font-size: 64px; letter-spacing: 4px;
    text-transform: uppercase;
    color: var(--ink);
  }
  .invite-names .amp { color: var(--gold); }
  .invite-line {
    position: absolute; left: 0; right: 0;
    text-align: center;
    text-transform: uppercase;
    font-size: 19px; letter-spacing: 2px; font-weight: 400;
  }
  .invite-intro { top: 540px; }
  .invite-date {
    top: 592px;
    font-family: "Limelight", serif;
    font-size: 46px; letter-spacing: 4px;
    color: var(--gold);
  }
  .invite-time { top: 724px; }
  .invite-venue { top: 756px; }

  /* Dividers and ornaments */
  .divider {
    position: absolute; height: 3px; background: var(--gold);
  }
  .divider::before, .divider::after {
    content: ""; position: absolute; top: -3px; width: 9px; height: 9px;
    border-radius: 50%; background: var(--gold);
  }
  .divider::before { left: -4px; }
  .divider::after { right: -4px; }
  .divider.thin { height: 1px; }
  .divider.thin::before, .divider.thin::after { top: -3px; width: 7px; height: 7px; }
  .ornament {
    position: absolute;
    background: linear-gradient(to right, var(--paper), var(--gold-light) 30%, var(--gold) 50%, var(--gold-light) 70%, var(--paper));
    border-radius: 50%;
  }
  .corner {
    position: absolute; width: 92px; height: 150px;
    background: linear-gradient(to top, var(--gold-light), var(--gold-pale) 70%, var(--paper));
  }
  .corner.left { left: 26px; bottom: 30px; border-top-right-radius: 60px; }
  .corner.right { right: 26px; bottom: 30px; border-top-left-radius: 60px; }
</style>
</head>
<body>

  <section class="card cover">
    <div class="cover-circles" role="img" aria-label="Cluster of gold concentric Art Deco circles"></div>
    <h2 class="cover-names">Rowan &amp; Liesel</h2>
    <div class="divider" style="left:44px; width:328px; top:292px;"></div>
    <div class="ornament" role="img" aria-label="Gold Art Deco scroll flourish" style="left:128px; top:302px; width:160px; height:26px;"></div>
  </section>

  <section class="card pattern-card">
    <div class="pattern-fill" role="img" aria-label="All-over pattern of gold concentric Art Deco circles"></div>
  </section>

  <section class="card invitation">
    <div class="invite-circles" role="img" aria-label="Band of overlapping gold concentric Art Deco circles"></div>
    <h1 class="invite-names">Rowan <span class="amp">&amp;</span> Liesel</h1>
    <div class="divider" style="left:45px; width:610px; top:432px;"></div>
    <div class="ornament" role="img" aria-label="Gold Art Deco scroll flourish" style="left:255px; top:443px; width:190px; height:34px;"></div>

    <p class="invite-line invite-intro">Invite you to celebrate their marriage</p>
    <p class="invite-line invite-date">May 8, 2015.</p>
    <div class="divider thin" style="left:130px; width:440px; top:675px;"></div>
    <div class="ornament" role="img" aria-label="Small gold Art Deco motif" style="left:335px; top:666px; width:30px; height:30px;"></div>

    <p class="invite-line invite-time">At four o' clock in the afternoon</p>
    <p class="invite-line invite-venue">St. Agnes Chapel Berlin</p>

    <div class="corner left" role="img" aria-label="Gold Art Deco corner flourish"></div>
    <div class="corner right" role="img" aria-label="Gold Art Deco corner flourish"></div>
  </section>

</body>
</html>
```